Business Card Design Project

Business Card design based on logo.

I need business card, letterhead, envelope, and if possible, Powerpoint slide template.

On front of business card: Just logo- and  my name and title:  Rosalind Pekar, Principal

On reverse-logo and the rest of the contact info:

4857 Orchard Lane
Fairmont Hills, CA 95699
650-381-2276
rp@brindlestudyworks.example

On letterhead-Just logo at top, at bottom  the rest-very small along the bottom

On PPT slide-just the logo.

I also want to try a few other colors-I like lime/dark grey (not black) but would like to try Sienna, maybe also indigo or bright blue-green.

I forgot to add-

On the business card-switch to vertical on reverse side and put:

Reverse side-switch to vertical and list:

Rosalind Pekar
Principal
Brindle Study Works, LLC

650-381-2276

4857 Orchard Lane
Fairmont Hills, CA 95699

Rosalind Pekar
Principal

650-381-2276

4857 Orchard Lane
Fairmont Hills, CA 95699

I have another project at the same time-for Stationery. Feel free to submit to that one also.

That one includes letterhead, envelope, PPT slide, folder cover sheet-RP

Industry/Entity Type

Business

Requirements
Must have
• Must use logo-preferably lime green version-with gray, not black or just 2-tone -logo on colored background.

```html
<!DOCTYPE html>
<html lang="en">
<head>
<meta charset="utf-8">
<title>Brindle Study Works — Business Card</title>
<link rel="stylesheet" href="https://fonts.googleapis.com/css2?family=Lato:wght@400;700&display=swap">
<style>
  :root {
    --backdrop: #d9d9d9;
    --card-dark: #4a4b4d;
    --card-light: #f4f4f2;
    --lime: #8cb832;
    --ink: #4d4d4f;
    --ink-soft: #5e5e60;
    --rule: #7a7a7a;
    --on-dark: #f1f1ef;
  }
  html, body {
    margin: 0;
    width: 1200px;
    height: 747px;
    overflow: hidden;
    background: var(--backdrop);
    font-family: "Lato", sans-serif;
  }
  .stage {
    position: relative;
    width: 1200px;
    height: 747px;
  }
  .card {
    position: absolute;
    top: 88px;
    width: 340px;
    height: 580px;
    overflow: hidden;
    box-shadow: 0 6px 18px rgba(0,0,0,0.18);
  }
  .card--front {
    left: 190px;
    background: var(--card-dark);
  }
  .card--back {
    left: 670px;
    background: var(--card-light);
    color: var(--ink);
  }

  /* Front: vertical wordmark */
  .front-mark {
    position: absolute;
    left: 50%;
    top: 50%;
    transform: translate(-50%, -50%) rotate(-90deg);
    display: flex;
    align-items: center;
    gap: 16px;
    white-space: nowrap;
  }
  .front-mark__square {
    flex: none;
    width: 26px;
    height: 26px;
    background: var(--lime);
  }
  .front-mark__name {
    font-size: 30px;
    font-weight: 400;
    letter-spacing: 3px;
    color: var(--on-dark);
    text-transform: uppercase;
  }

  /* Back: contact details */
  .identity {
    position: absolute;
    left: 32px;
    right: 32px;
    top: 42px;
  }
  .identity__name {
    margin: 0;
    font-size: 26px;
    font-weight: 400;
    letter-spacing: 1px;
    text-transform: uppercase;
  }
  .identity__title,
  .identity__company {
    margin: 4px 0 0;
    font-size: 18px;
    color: var(--ink-soft);
  }
  .identity__rule {
    margin: 22px 0 0;
    border: 0;
    border-top: 1.5px solid var(--rule);
  }
  .contact {
    position: absolute;
    left: 32px;
    right: 20px;
    top: 210px;
    font-size: 17px;
    color: var(--ink);
  }
  .contact__row {
    display: flex;
    align-items: center;
    gap: 14px;
    margin-bottom: 6px;
  }
  .contact__row--address {
    align-items: flex-start;
    margin-top: 26px;
    line-height: 1.35;
  }
  .contact__icon {
    flex: none;
    width: 18px;
    height: 16px;
  }
  .contact__row--address .contact__icon {
    margin-top: 3px;
  }
  .back-mark {
    position: absolute;
    left: 0;
    right: 0;
    bottom: 46px;
    display: flex;
    justify-content: center;
    align-items: center;
    gap: 10px;
    white-space: nowrap;
  }
  .back-mark__square {
    flex: none;
    width: 16px;
    height: 16px;
    background: var(--lime);
  }
  .back-mark__name {
    font-size: 19px;
    font-weight: 400;
    letter-spacing: 1.5px;
    color: var(--ink);
    text-transform: uppercase;
  }
</style>
</head>
<body>
<main class="stage">
  <section class="card card--front" aria-label="Business card front">
    <div class="front-mark">
      <span class="front-mark__square"></span>
      <span class="front-mark__name">Brindle Study Works</span>
    </div>
  </section>

  <section class="card card--back" aria-label="Business card back">
    <div class="identity">
      <h1 class="identity__name">Rosalind Pekar</h1>
      <p class="identity__title">Principal</p>
      <p class="identity__company">Brindle Study Works, LLC</p>
      <hr class="identity__rule">
    </div>

    <div class="contact">
      <div class="contact__row">
        <svg class="contact__icon" viewBox="0 0 18 16" aria-hidden="true">
          <rect x="1" y="1" width="16" height="14" rx="2" fill="none" stroke="#8cb832" stroke-width="1.6"/>
          <rect x="4" y="4" width="4" height="8" fill="#8cb832"/>
          <rect x="10" y="4" width="4" height="2" fill="#8cb832"/>
          <rect x="10" y="8" width="4" height="4" fill="#8cb832"/>
        </svg>
        <span>650-381-2276</span>
      </div>
      <div class="contact__row">
        <svg class="contact__icon" viewBox="0 0 18 16" aria-hidden="true">
          <rect x="1" y="2" width="16" height="12" fill="none" stroke="#8cb832" stroke-width="1.6"/>
          <path d="M1 2 L9 9 L17 2 M1 14 L7 8 M17 14 L11 8" fill="none" stroke="#8cb832" stroke-width="1.4"/>
        </svg>
        <span>rp@brindlestudyworks.example</span>
      </div>
      <div class="contact__row contact__row--address">
        <svg class="contact__icon" viewBox="0 0 18 16" aria-hidden="true">
          <path d="M9 15 C5 10 4 8 4 6 A5 5 0 0 1 14 6 C14 8 13 10 9 15 Z" fill="#8cb832"/>
          <circle cx="9" cy="6" r="2" fill="#f4f4f2"/>
        </svg>
        <span>4857 Orchard Lane<br>Fairmont Hills, CA 95699</span>
      </div>
    </div>

    <div class="back-mark">
      <span class="back-mark__square"></span>
      <span class="back-mark__name">Brindle Study Works</span>
    </div>
  </section>
</main>
</body>
</html>
```